Simple Business Cards for Self-employed Coach

Simple business card with a design that includes the QLT logo.
Using either only the logo color or additional colors that match the logo.

Meridian Guides reach deeply into the past, gathering wisdom from East and West, while still staying current with the frontiers of new discovery in cognitive science, genetics, and other disciplines. see https://www.brightharborpath.example/what-is-integral-coaching/

Target Market(s)

Coaching Clients in Tokyo /Asia; in business organizations, but also outside

Industry/Entity Type

Life Coaching

Contact Information for Business Card

Lukas Brenning
Certified Meridian Guide

3-2-48 Kamiyoshi
Nakarino 164-0392
Tokyo, Japan

Phone: +81 70 4817 5062
E-Mail: lukas.brenning@mailora.example

Font styles to use
Sans Serif

Colors
00a990

Requirements
Must have
• include uploaded logo
• color fitting with QLT logo color
Nice to have
• simple, elegant design
Should not have
• clutter

```html
<!DOCTYPE html>
<html lang="en">
<head>
<meta charset="utf-8">
<title>Lukas Brenning – Business Card</title>
<link rel="stylesheet" href="https://fonts.googleapis.com/css2?family=Quicksand:wght@400;500;600&display=swap">
<style>
  :root {
    --bg: #1e1e1e;
    --teal: #16b394;
    --teal-deep: #0e7f6a;
    --teal-text: #1cc3a0;
    --stripe: #5ccf95;
    --grey: #7b7b7b;
    --contact: #3fd8a8;
  }
  html, body {
    margin: 0;
    width: 1200px;
    height: 837px;
    overflow: hidden;
    background: var(--bg);
    font-family: "Quicksand", sans-serif;
  }
  .card {
    position: absolute;
    left: 100px;
    top: 128px;
    width: 1000px;
    height: 580px;
    border-radius: 34px;
    overflow: hidden;
    background: var(--grey);
  }
  .card-top {
    position: absolute;
    inset: 0 0 auto 0;
    height: 330px;
    background: var(--teal);
  }
  .card-pattern {
    position: absolute;
    inset: 0;
    background: linear-gradient(135deg, #19b998 0%, #13ab8d 100%);
  }
  .brand {
    position: absolute;
    left: 50%;
    top: 50%;
    transform: translate(-50%, -50%);
    display: flex;
    align-items: center;
    gap: 22px;
  }
  .brand-mark {
    width: 44px;
    height: 44px;
    background: var(--teal-deep);
  }
  .brand-name {
    font-size: 110px;
    font-weight: 600;
    letter-spacing: 0.18em;
    color: var(--teal-deep);
    line-height: 1;
  }
  .card-stripe {
    position: absolute;
    left: 0; right: 0;
    top: 330px;
    height: 24px;
    background: var(--stripe);
  }
  .holder {
    position: absolute;
    left: 70px;
    top: 374px;
    color: var(--teal-text);
  }
  .holder-name {
    margin: 0;
    font-size: 50px;
    font-weight: 500;
    line-height: 1.05;
  }
  .holder-title {
    margin: 2px 0 0;
    font-size: 25px;
    font-weight: 500;
  }
  .contact {
    position: absolute;
    left: 70px;
    display: flex;
    align-items: center;
    gap: 12px;
    font-size: 23px;
    font-weight: 500;
    color: var(--contact);
  }
  .contact-phone { top: 476px; }
  .contact-mail { top: 516px; }
  .contact svg { flex: none; }
  .address {
    position: absolute;
    right: 60px;
    bottom: 38px;
    margin: 0;
    text-align: right;
    font-style: normal;
    font-size: 25px;
    font-weight: 500;
    line-height: 1.4;
    color: var(--teal-text);
  }
</style>
</head>
<body>
  <div class="card">
    <div class="card-top">
      <div class="card-pattern" role="img" aria-label="Repeating pattern of small outlined light bulbs on teal"></div>
      <div class="brand">
        <span class="brand-mark"></span>
        <span class="brand-name">QLT</span>
      </div>
    </div>
    <div class="card-stripe"></div>

    <div class="holder">
      <p class="holder-name">Lukas Brenning</p>
      <p class="holder-title">Certified Meridian Guide</p>
    </div>

    <div class="contact contact-phone">
      <svg width="26" height="26" viewBox="0 0 26 26" aria-hidden="true">
        <rect width="26" height="26" rx="5" fill="var(--stripe)"/>
        <path d="M9 6c-1.5 0-2.5 1.5-2 3.5 1 4 4.5 8 9 9.5 2 .5 3.5-.5 3.5-2l-3-2-1.5 1.5c-2-1-3.5-2.5-4.5-4.5L12 10.5 9 6z" fill="#5a5a5a"/>
      </svg>
      <span>+81 70 4817 5062</span>
    </div>

    <div class="contact contact-mail">
      <svg width="28" height="20" viewBox="0 0 28 20" aria-hidden="true">
        <rect x="1" y="1" width="26" height="18" rx="2" fill="none" stroke="var(--contact)" stroke-width="2"/>
        <path d="M1 2l13 10L27 2" fill="none" stroke="var(--contact)" stroke-width="2"/>
      </svg>
      <span>lukas.brenning@mailora.example</span>
    </div>

    <address class="address">
      3-2-48 Kamiyoshi<br>
      Nakarino 164-0392<br>
      Tokyo, Japan
    </address>
  </div>
</body>
</html>
```